Four banner campaigns, much work to come!

I want banners created for 4 campaigns.

For each campaign I need these 6 banner sizes created:

? Web Banner Sizes (300x250, 728x90, 160x600)
One of each of these sizes, so 3 web banners

? Mobile Banner Sizes (300x50, 216x36, 240x240)

Campaign 1
http://www.townshopratings.example/KVB-52917.html

Campaign 2
http://www.townshopratings.example/Rockville-MD/Velunor-48203.html

Campaign 3
http://www.nearbylistpages.example/m/orlando-fl-vacation-rentals/

Campaign 4
www.townshopratings.example/The-Hollis-Institute-of-Sound-and-Screen-Studies-73542.html

I will send you numbers to edit each banner, so the 24 banners
will have 4 variations with different numbers. Same banners just
need you to send a copy with different phone numbers.

I want the work done today and I will post my next gig for the same winner.
Updates

I just want to make sure everyone knows this project is for 4 different banner campaigns.

Given banners in each size for each campaign.  I can submit additional info links if
needed let me know.  Please post more samples as soon as possible so I can pick
a designer to finish.

Thank you!

Industry/Entity Type

Radio

Requirements
Must have
• Messaging that follows the messaging in the pages I have submitted.
Nice to have
• Animated gif banners in general, QDN compliant.

```html
<!DOCTYPE html>
<html lang="en">
<head>
<meta charset="utf-8">
<title>The Hollis Institute – Banner Set</title>
<link rel="stylesheet" href="https://fonts.googleapis.com/css2?family=Arimo:wght@400;700&display=swap">
<style>
  :root{
    --stage-top:#ececec;
    --stage-bottom:#c6c6c6;
    --night:#05070c;
    --navy:#1a2f4d;
    --steel:#3b5a80;
    --white:#ffffff;
    --lime-top:#eaff6a;
    --lime-bottom:#a6d916;
    --lime-edge:#7fae0a;
    --photo-red:#d9352a;
    --photo-grey:#6c6f74;
  }
  *{box-sizing:border-box;margin:0;padding:0}
  html,body{width:1200px;height:780px;overflow:hidden}
  body{
    background:linear-gradient(180deg,var(--stage-top),var(--stage-bottom));
    font-family:"Arimo",Arial,sans-serif;color:var(--white);position:relative;
  }
  .banner{
    position:absolute;overflow:hidden;
    background:
      radial-gradient(ellipse at 40% 70%,rgba(59,90,128,.75),transparent 65%),
      linear-gradient(180deg,var(--night) 0%,var(--navy) 55%,var(--night) 100%);
  }
  .banner svg.art{position:absolute;left:0;top:0}
  .brand{position:absolute;font-weight:700;color:var(--white);line-height:1.05}
  .brand .name{display:block}
  .brand .sub{display:block;font-size:.42em;margin-top:2px}
  .headline{position:absolute;text-align:center;line-height:1.25}
  .cta{position:absolute;text-align:center;font-weight:400}
  .phone{
    position:absolute;display:flex;align-items:center;justify-content:center;
    color:#000;font-weight:400;border-radius:6px;
    background:linear-gradient(180deg,var(--lime-top),var(--lime-bottom));
    border:1px solid var(--lime-edge);
  }

  /* Skyscraper 160x600 */
  .sky{left:47px;top:41px;width:188px;height:702px}
  .sky .brand{left:10px;top:172px;font-size:17px}
  .sky .lead{position:absolute;left:0;width:100%;top:318px;text-align:center;font-size:42px}
  .sky .headline{left:0;width:100%;top:378px;font-size:27px;line-height:1.55}
  .sky .cta{left:0;width:100%;top:592px;font-size:35px}
  .sky .phone{left:8px;top:643px;width:172px;height:42px;font-size:21px}

  /* Medium rectangle */
  .rect{left:407px;top:296px;width:281px;height:280px}
  .rect .logo-box{position:absolute;left:0;top:22px;width:165px;height:50px;background:var(--night)}
  .rect .brand{left:7px;top:30px;font-size:15px}
  .rect .headline{left:0;width:100%;top:108px;font-size:21px}
  .rect .cta{left:0;width:100%;top:184px;font-size:28px}
  .rect .phone{left:27px;top:227px;width:224px;height:40px;font-size:23px}

  /* Square */
  .square{left:734px;top:291px;width:352px;height:292px}
  .square .logo-box{position:absolute;left:0;top:25px;width:190px;height:58px;background:var(--night)}
  .square .brand{left:10px;top:34px;font-size:17px}
  .square .headline{left:0;width:100%;top:120px;font-size:25px}
  .square .cta{left:0;width:100%;top:199px;font-size:29px}
  .square .phone{left:61px;top:242px;width:224px;height:42px;font-size:24px}

  /* Leaderboard */
  .leader{left:261px;top:639px;width:852px;height:104px}
  .leader .brand{left:14px;top:24px;font-size:30px}
  .leader .brand .sub{font-size:.42em}
  .leader .headline{left:305px;top:22px;font-size:25px;text-align:left;line-height:1.35}
  .leader .phone{left:672px;top:58px;width:170px;height:38px;font-size:21px}
</style>
</head>
<body>

  <!-- Skyscraper -->
  <section class="banner sky">
    <svg class="art" width="188" height="200" viewBox="0 0 188 200">
      <polygon points="34,0 188,0 188,122 76,150" fill="url(#photoTone)" role="img" aria-label="Photo of a smiling radio host with red hair wearing headphones in a studio"/>
      <polygon points="14,0 34,0 76,150 188,122 188,136 68,172" fill="var(--white)"/>
      <defs>
        <linearGradient id="photoTone" x1="0" y1="0" x2="1" y2="1">
          <stop offset="0" stop-color="var(--photo-grey)"/>
          <stop offset=".5" stop-color="var(--photo-red)"/>
          <stop offset="1" stop-color="#2a2c30"/>
        </linearGradient>
      </defs>
    </svg>
    <div class="brand"><span class="name">The Hollis Institute</span><span class="sub">OF SOUND &amp; SCREEN STUDIES</span></div>
    <p class="lead">Make</p>
    <p class="headline">the career<br>change that<br>can change<br>your life</p>
    <p class="cta">Call Now!</p>
    <div class="phone">(888) 555-0147</div>
  </section>

  <!-- Medium rectangle -->
  <section class="banner rect">
    <svg class="art" width="281" height="100" viewBox="0 0 281 100">
      <polygon points="126,0 281,0 281,66 166,92" fill="url(#photoTone2)" role="img" aria-label="Photo of a smiling radio host with red hair wearing headphones in a studio"/>
      <polygon points="112,0 126,0 166,92 281,66 281,76 160,102" fill="var(--white)"/>
      <defs>
        <linearGradient id="photoTone2" x1="0" y1="0" x2="1" y2="1">
          <stop offset="0" stop-color="var(--photo-grey)"/>
          <stop offset=".5" stop-color="var(--photo-red)"/>
          <stop offset="1" stop-color="#2a2c30"/>
        </linearGradient>
      </defs>
    </svg>
    <div class="logo-box"></div>
    <div class="brand"><span class="name">The Hollis Institute</span><span class="sub">OF SOUND &amp; SCREEN STUDIES</span></div>
    <p class="headline">Make the career change<br>that can change your life</p>
    <p class="cta">Call Now!</p>
    <div class="phone">(888) 555-0147</div>
  </section>

  <!-- Square -->
  <section class="banner square">
    <svg class="art" width="352" height="130" viewBox="0 0 352 130">
      <polygon points="160,0 352,0 352,100 236,122" fill="url(#photoTone3)" role="img" aria-label="Photo of a smiling radio host with red hair wearing headphones at a studio microphone"/>
      <polygon points="144,0 160,0 236,122 352,100 352,112 228,134" fill="var(--white)"/>
      <defs>
        <linearGradient id="photoTone3" x1="0" y1="0" x2="1" y2="1">
          <stop offset="0" stop-color="var(--photo-grey)"/>
          <stop offset=".5" stop-color="var(--photo-red)"/>
          <stop offset="1" stop-color="#2a2c30"/>
        </linearGradient>
      </defs>
    </svg>
    <div class="logo-box"></div>
    <div class="brand"><span class="name">The Hollis Institute</span><span class="sub">OF SOUND &amp; SCREEN STUDIES</span></div>
    <p class="headline">Make the career change<br>that can change your life</p>
    <p class="cta">Call Now!</p>
    <div class="phone">(888) 555-0147</div>
  </section>

  <!-- Leaderboard -->
  <section class="banner leader">
    <svg class="art" width="852" height="104" viewBox="0 0 852 104">
      <polygon points="0,0 300,0 300,104 0,104" fill="var(--night)"/>
      <polygon points="650,0 852,0 852,104 690,104" fill="url(#photoTone4)" role="img" aria-label="Photo of a smiling radio host with red hair wearing headphones in a studio"/>
      <polygon points="636,0 650,0 690,104 676,104" fill="var(--white)"/>
      <defs>
        <linearGradient id="photoTone4" x1="0" y1="0" x2="1" y2="1">
          <stop offset="0" stop-color="var(--photo-red)"/>
          <stop offset=".6" stop-color="var(--photo-grey)"/>
          <stop offset="1" stop-color="#2a2c30"/>
        </linearGradient>
      </defs>
    </svg>
    <div class="brand"><span class="name">The Hollis Institute</span><span class="sub">OF SOUND &amp; SCREEN STUDIES</span></div>
    <p class="headline">Make the career change<br>that can change your life</p>
    <div class="phone">(888) 555-0147</div>
  </section>

</body>
</html>
```